Political Mail Out Quintero front and back

Front
Esteban (9th Grade) Quintero!

What's that famous saying?

Show me who your friends are and I'll tell you who you really are!
(show the two guys)

Arturo Benavides is charged with voter fraud by changing voter addresses from across the RGV so they could vote in Edinburg
Back
Did Esteban (9th Grade) Quintero commit voter fraud when he ran for office in 2016?
(insert blurred photo)

Here is a list of people from all over the RGV that voted in Edinburg in the 2016 race.
Here is a break down:

(highlight the number and where they were first registered to vote)

9 People voted in Edinburg who were registered in Donna.
13 People voted in Edinburg who were registered in San Juan
8 People voted in Edinburg who were registered in Pharr
31 People voted in Edinburg who were registered in McAllen
2 People voted in Edinburg who were registered in La Joya
6 People voted in Edinburg who were registered in Edcouch
2 People voted in Edinburg who were registered in Mercedes
2 People voted in Edinburg who were registered in Monte Alto
6 People voted in Edinburg who were registered in Weslaco
1 Person voted in Edinburg who were registered in Penitas
3 People voted in Edinburg who were registered in Alamo
5 People voted in Edinburg who were registered in Elsa
6 People voted in Edinburg who were registered in Mission
1 Person voted in Edinburg who were registered in Alton

Will Esteban (9th Grade) Quintero CHEAT in 2020?

Only time will tell.

Vote Esteban (9th Grade) Quintero OUT of office.

```html
<!DOCTYPE html>
<html lang="en">
<head>
<meta charset="utf-8">
<title>Quintero Mailer – Front and Back</title>
<link href="https://fonts.googleapis.com/css2?family=Barlow+Condensed:ital,wght@0,500;0,700;1,500;1,700;1,800&family=Barlow:ital,wght@0,400;0,700;1,700;1,800&display=swap" rel="stylesheet">
<style>
  :root{
    --bg:#434244;
    --blue:#1c75bc;
    --red:#ed1c24;
    --yellow:#fff200;
    --navy:#1d2a6b;
    --paper:#f1f2f2;
    --white:#ffffff;
    --ink:#111111;
    --rule:#bcbec0;
  }
  *{margin:0;padding:0;box-sizing:border-box}
  html,body{width:842px;height:1200px;overflow:hidden;background:var(--bg)}
  body{position:relative;font-family:"Barlow",sans-serif}
  .card{position:absolute;left:92px;width:658px;height:470px;overflow:hidden}
  .front{top:114px;background:var(--blue)}
  .back{top:616px;background:var(--paper)}
  .cond{font-family:"Barlow Condensed",sans-serif;font-style:italic}

  .front-title{position:absolute;top:12px;left:0;width:100%;text-align:center;color:var(--white);font-size:42px;font-weight:800;letter-spacing:-1px;text-shadow:2px 2px 0 var(--red)}
  .photo-frame{position:absolute;left:90px;top:72px;width:477px;height:299px;background:var(--white)}
  .photo{position:absolute;left:13px;top:13px;width:451px;height:274px;background:linear-gradient(90deg,#b89a80 0%,#d6c3ae 40%,#6f6d69 70%,#4d3a2a 100%)}
  .saying{position:absolute;left:134px;top:325px;width:390px;height:84px;background:var(--red);text-align:center;color:var(--white)}
  .saying .kicker{display:block;margin-top:10px;color:var(--yellow);font-size:12px;font-weight:700}
  .saying .quote{display:block;font-size:27px;font-weight:800;line-height:29px;letter-spacing:-.5px}
  .charge{position:absolute;top:417px;left:0;width:100%;text-align:center;color:var(--white);font-size:17.5px;font-weight:500;line-height:19px}
  .charge b{font-weight:800}

  .back-red{position:absolute;left:0;top:0;width:404px;height:146px;background:var(--red)}
  .address-side{position:absolute;left:404px;top:0;width:254px;height:359px;background:var(--white)}
  .stamp{position:absolute;left:153px;top:29px;width:72px;height:71px;border:1px solid #9a9a9a}
  .address-line{position:absolute;left:42px;width:183px;height:1px;background:var(--rule)}
  .back-title{position:absolute;left:35px;top:17px;color:var(--white);font-size:23.5px;font-weight:800;line-height:24px;letter-spacing:-.4px}
  .records{position:absolute;left:35px;top:70px;width:329px;height:130px;background:var(--navy)}
  .records-text{position:absolute;left:0;top:35px;width:100%;padding-left:44px;text-align:center;color:var(--white);font-size:16.5px;font-weight:800;line-height:21px;letter-spacing:-.3px}
  .tally{position:absolute;left:44px;top:222px;width:90px;text-align:center;color:var(--red);font-weight:800}
  .tally .over,.tally .votes{display:block;font-size:25px;line-height:24px}
  .tally .num{display:block;font-size:92px;line-height:78px;letter-spacing:-4px}
  .divider{position:absolute;left:157px;top:225px;width:2px;height:117px;background:#a7a9ac}
  .breakdown{position:absolute;left:171px;top:211px;list-style:none;font-size:7.6px;line-height:10.15px;color:var(--ink);letter-spacing:-.1px}
  .breakdown b{font-weight:700}
  .breakdown em{font-weight:800;font-style:italic}
  .warning{position:absolute;left:0;top:359px;width:100%;height:33px;background:var(--yellow);text-align:center;font-size:17.5px;line-height:33px;color:var(--ink)}
  .warning strong{font-family:"Barlow",sans-serif;font-style:italic;font-weight:800;font-size:15.5px}
  .call{position:absolute;left:0;top:392px;width:100%;height:78px;background:var(--red);color:var(--white)}
  .call svg{position:absolute;left:60px;top:15px}
  .call-text{position:absolute;left:120px;top:17px;font-size:31px;font-weight:800;letter-spacing:-.6px}
</style>
</head>
<body>

<section class="card front">
  <h1 class="front-title cond">Esteban (9th Grade) Quintero!</h1>
  <div class="photo-frame">
    <div class="photo" role="img" aria-label="Photo of two smiling men posing together in campaign polo shirts"></div>
  </div>
  <div class="saying cond">
    <span class="kicker">WHAT’S THAT FAMOUS SAYING?</span>
    <span class="quote">Show me who your friends are and<br>I’ll tell you who you really are!</span>
  </div>
  <p class="charge cond"><b>Arturo Benavides is charged</b> with voter fraud by changing voter<br>addresses from across the RGV so they could vote in Edinburg</p>
</section>

<section class="card back">
  <div class="back-red"></div>
  <div class="address-side">
    <div class="stamp"></div>
    <div class="address-line" style="top:154px"></div>
    <div class="address-line" style="top:179px"></div>
    <div class="address-line" style="top:203px"></div>
    <div class="address-line" style="top:227px"></div>
    <div class="address-line" style="top:252px"></div>
    <div class="address-line" style="top:276px"></div>
    <div class="address-line" style="top:300px"></div>
  </div>
  <h2 class="back-title cond">Did Esteban (9th Grade) Quintero commit<br>voter fraud when he ran for office in 2016?</h2>
  <div class="records" role="img" aria-label="Blurred photo of a voter registration spreadsheet">
    <p class="records-text cond">Here is a list of people from all over the<br>RGV that voted in Edinburg in the 2016<br>race. Here is a break down:</p>
  </div>
  <div class="tally cond"><span class="over">OVER</span><span class="num">95</span><span class="votes">VOTES</span></div>
  <div class="divider"></div>
  <ul class="breakdown">
    <li><b>9 People</b> voted in Edinburg who were <em>registered in Donna.</em></li>
    <li><b>13 People</b> voted in Edinburg who were <em>registered in San Juan</em></li>
    <li><b>8 People</b> voted in Edinburg who were <em>registered in Pharr</em></li>
    <li><b>31 People</b> voted in Edinburg who were <em>registered in McAllen</em></li>
    <li><b>2 People</b> voted in Edinburg who were <em>registered in La Joya</em></li>
    <li><b>6 People</b> voted in Edinburg who were <em>registered in Edcouch</em></li>
    <li><b>2 People</b> voted in Edinburg who were <em>registered in Mercedes</em></li>
    <li><b>2 People</b> voted in Edinburg who were <em>registered in Monte Alto</em></li>
    <li><b>6 People</b> voted in Edinburg who were <em>registered in Weslaco</em></li>
    <li><b>1 Person</b> voted in Edinburg who were <em>registered in Penitas</em></li>
    <li><b>3 People</b> voted in Edinburg who were <em>registered in Alamo</em></li>
    <li><b>5 People</b> voted in Edinburg who were <em>registered in Elsa</em></li>
    <li><b>6 People</b> voted in Edinburg who were <em>registered in Mission</em></li>
    <li><b>1 Person</b> voted in Edinburg who were <em>registered in Alton</em></li>
  </ul>
  <p class="warning cond"><strong>Will Esteban (9th Grade) Quintero CHEAT in 2020?</strong> Only time will tell.</p>
  <div class="call">
    <svg width="50" height="50" viewBox="0 0 50 50" aria-hidden="true">
      <circle cx="25" cy="25" r="22" fill="none" stroke="#fff" stroke-width="5"/>
      <path d="M17 17 L33 33 M33 17 L17 33" stroke="#fff" stroke-width="6" stroke-linecap="round"/>
    </svg>
    <p class="call-text cond">Vote Esteban (9th Grade) Quintero OUT of office</p>
  </div>
</section>

</body>
</html>
```